Business sign to place on building

I am interested in installing a sign on the building located at 457 Carrow Ave, Tonawanda, NY 14150. The sign we be equipped with components to enable illumination.

we would like :
the (small)
BRISTLECONE (large like in the sign we like in attach)
events & gathering space (small)

Attached below, you will find:

An image of the building.
The designated location where the sign will be installed.
A reference image of a sign that we particularly like.
The Bristlecone logo

The Bristlecone is a Events venue
www.thebristlecone-example.com

The Bristlecone event venue

```html
<!DOCTYPE html>
<html lang="en">
<head>
<meta charset="utf-8">
<title>The Bristlecone Event Venue – Building Sign</title>
<link rel="stylesheet" href="https://fonts.googleapis.com/css2?family=Montserrat:wght@500;700&family=Yellowtail&display=swap">
<style>
  :root {
    --sign-bg: #45100c;
    --sign-ink: #ffffff;
    --page-bg: #ffffff;
  }
  html, body {
    margin: 0;
    padding: 0;
    width: 1200px;
    height: 1003px;
    overflow: hidden;
    background: var(--page-bg);
  }
  .canvas {
    position: relative;
    width: 1200px;
    height: 1003px;
  }
  .sign {
    position: absolute;
    left: 80px;
    top: 242px;
    width: 1040px;
    height: 518px;
    background: var(--sign-bg);
  }
  .sign svg {
    display: block;
    width: 100%;
    height: 100%;
  }
  .brand-the {
    font-family: 'Montserrat', sans-serif;
    font-weight: 700;
    font-size: 15px;
    fill: var(--sign-ink);
  }
  .brand-name {
    font-family: 'Montserrat', sans-serif;
    font-weight: 700;
    font-size: 24px;
    fill: var(--sign-ink);
  }
  .title-the {
    font-family: 'Montserrat', sans-serif;
    font-weight: 500;
    font-size: 30px;
    letter-spacing: 2px;
    fill: var(--sign-ink);
  }
  .title-script {
    font-family: 'Yellowtail', cursive;
    font-size: 210px;
    fill: var(--sign-ink);
  }
  .tagline {
    font-family: 'Montserrat', sans-serif;
    font-weight: 500;
    font-size: 31px;
    letter-spacing: 9px;
    fill: var(--sign-ink);
  }
</style>
</head>
<body>
  <main class="canvas">
    <section class="sign" aria-label="The Bristlecone Event Venue sign">
      <svg viewBox="0 0 1040 518" xmlns="http://www.w3.org/2000/svg">
        <g class="brand-lockup">
          <text class="brand-the" x="520" y="50" text-anchor="middle">THE</text>
          <text class="brand-name" x="520" y="88" text-anchor="middle" letter-spacing="1">BRISTLECONE</text>
        </g>
        <text class="title-the" x="214" y="183">THE</text>
        <text class="title-script" x="44" y="352" textLength="950" lengthAdjust="spacingAndGlyphs">Bristlecone</text>
        <text class="tagline" x="337" y="434">EVENT</text>
        <text class="tagline" x="624" y="434">VENUE</text>
      </svg>
    </section>
  </main>
</body>
</html>
```